Label for flatbread

create an innovative and visually appealing label for flatbread packaging. The goal is to blend traditional bread-making heritage with a modern aesthetic that attracts consumers in retail environments while communicating freshness, quality, and authenticity.

To design a front-facing package label for flatbread that:
• Captures the essence of artisanal baking and cultural tradition.
• Stands out on shelves with strong visual appeal.
• You can use folk art to create the images on the label, elements like flatbread, wheat,
We want to print the label in a sticker and put it on bread bag, so consider that you are designing a label in a frame for instance 4 inch in 5 inch rectangular. We would like that the label has theme like the uploaded images (does not need to be similar to the uploaded images) these images give you a clue .

Target Market(s)

Groceries stores in Vancouver area Canada

Industry/Entity Type

Bakery

Font styles to use
Other font styles liked:
• feel free to choose your font yourself

Requirements
Must have
• Design the label to attract consumers and encourage them to choose this bread. Create an eye-catching label that entices consumers to try this bread. Make the label so appealing that consumers can’t resist picking up this bread.
Nice to have
• Clean, Illustration or icon of flatbread, Subtle grain (whole wheat!) or flour textures in the background to suggest craftsmanship, Made in Canada
Should not have
• we do not limit artists, use your imagination, do not put bread picture, the bread picture must be hand drawn

```html
<!DOCTYPE html>
<html lang="en">
<head>
<meta charset="utf-8">
<title>Traditional Flat Bread – Label</title>
<link rel="stylesheet" href="https://fonts.googleapis.com/css2?family=Lobster&family=Rye&family=Lexend:wght@700&family=Libre+Caslon+Text:wght@700&display=swap">
<style>
  :root {
    --page: #ffffff;
    --navy-deep: #0a1632;
    --navy: #14295a;
    --blue-mid: #1f5ea8;
    --blue-bright: #2aa7e6;
    --purple: #5b3a9a;
    --rust: #d2552b;
    --band-light: #c9d3e6;
    --disc: #dfe3ef;
    --disc-edge: #c2c8da;
    --ring: #08122b;
    --title-ink: #23205f;
    --tagline: #7a3f93;
    --crust-light: #f0dcae;
    --crust: #d9b077;
    --crust-dark: #a9743b;
    --wheat: #3a9fd4;
    --weight-text: #ffffff;
  }
  html, body {
    margin: 0;
    width: 1200px;
    height: 863px;
    overflow: hidden;
    background: var(--page);
  }
  .stage {
    width: 1200px;
    height: 863px;
    display: flex;
    align-items: center;
    justify-content: center;
  }
  .label { width: 573px; height: 800px; display: block; }
  .script-line { font-family: "Lobster", cursive; fill: var(--rust); }
  .product-name { font-family: "Rye", serif; fill: var(--title-ink); stroke: var(--title-ink); stroke-width: 7; stroke-linejoin: round; }
  .tagline { font-family: "Lexend", sans-serif; font-weight: 700; fill: var(--tagline); }
  .net-weight { font-family: "Libre Caslon Text", serif; font-weight: 700; fill: var(--weight-text); }
</style>
</head>
<body>
<main class="stage">
  <svg class="label" viewBox="0 0 1050 1465" xmlns="http://www.w3.org/2000/svg" aria-labelledby="label-title">
    <title id="label-title">Traditional Flat Bread label</title>
    <defs>
      <linearGradient id="base-tone" x1="0" y1="0" x2="0" y2="1">
        <stop offset="0" stop-color="var(--navy-deep)"/>
        <stop offset="0.5" stop-color="var(--navy)"/>
        <stop offset="0.75" stop-color="var(--blue-mid)"/>
        <stop offset="1" stop-color="var(--navy-deep)"/>
      </linearGradient>
      <radialGradient id="disc-tone" cx="0.5" cy="0.42" r="0.6">
        <stop offset="0" stop-color="var(--disc)"/>
        <stop offset="1" stop-color="var(--disc-edge)"/>
      </radialGradient>
      <linearGradient id="bread-tone" x1="0" y1="0" x2="0" y2="1">
        <stop offset="0" stop-color="var(--crust-light)"/>
        <stop offset="0.45" stop-color="var(--crust)"/>
        <stop offset="0.6" stop-color="var(--crust-light)"/>
        <stop offset="0.8" stop-color="var(--crust)"/>
        <stop offset="1" stop-color="var(--crust-dark)"/>
      </linearGradient>
    </defs>

    <!-- folk pattern area, shown as coloured bands -->
    <g class="folk-pattern" role="img" aria-label="Folk-art geometric pattern of zigzags, diamonds and triangles in blue, purple and orange">
      <rect x="0" y="0" width="1050" height="1465" fill="url(#base-tone)"/>
      <rect class="band band--blue" x="0" y="0" width="1050" height="22" fill="var(--blue-bright)" opacity="0.7"/>
      <rect class="band band--light" x="0" y="52" width="1050" height="26" fill="var(--band-light)" opacity="0.55"/>
      <rect class="band band--purple" x="0" y="108" width="1050" height="14" fill="var(--purple)"/>
      <rect class="band band--rust" x="0" y="160" width="1050" height="40" fill="var(--rust)" opacity="0.75"/>
      <rect class="band band--light" x="0" y="212" width="1050" height="8" fill="var(--band-light)" opacity="0.7"/>
      <rect class="band band--blue" x="0" y="232" width="1050" height="34" fill="var(--blue-bright)" opacity="0.6"/>
      <rect class="band band--purple" x="0" y="290" width="1050" height="30" fill="var(--purple)" opacity="0.85"/>
      <rect class="band band--rust" x="0" y="360" width="1050" height="46" fill="var(--rust)" opacity="0.7"/>
      <rect class="band band--blue" x="0" y="440" width="1050" height="40" fill="var(--blue-bright)" opacity="0.55"/>
      <rect class="band band--purple" x="0" y="530" width="1050" height="60" fill="var(--purple)" opacity="0.7"/>
      <rect class="band band--light" x="0" y="620" width="1050" height="14" fill="var(--band-light)" opacity="0.5"/>
      <rect class="band band--blue" x="0" y="690" width="1050" height="30" fill="var(--blue-bright)" opacity="0.5"/>
      <rect class="band band--rust" x="0" y="840" width="1050" height="46" fill="var(--rust)" opacity="0.75"/>
      <rect class="band band--purple" x="0" y="905" width="1050" height="20" fill="var(--purple)" opacity="0.8"/>
      <rect class="band band--light" x="0" y="950" width="1050" height="24" fill="var(--band-light)" opacity="0.6"/>
      <rect class="band band--blue" x="0" y="1000" width="1050" height="50" fill="var(--blue-bright)" opacity="0.8"/>
      <rect class="band band--purple" x="0" y="1075" width="1050" height="24" fill="var(--purple)" opacity="0.8"/>
      <rect class="band band--blue" x="0" y="1130" width="1050" height="34" fill="var(--blue-bright)" opacity="0.6"/>
      <rect class="band band--purple" x="0" y="1190" width="1050" height="18" fill="var(--purple)" opacity="0.9"/>
      <rect class="band band--rust" x="0" y="1230" width="1050" height="40" fill="var(--rust)" opacity="0.7"/>
      <rect class="band band--light" x="0" y="1290" width="1050" height="8" fill="var(--band-light)" opacity="0.7"/>
      <rect class="band band--blue" x="0" y="1320" width="1050" height="30" fill="var(--blue-bright)" opacity="0.6"/>
      <rect class="band band--purple" x="0" y="1375" width="1050" height="14" fill="var(--purple)"/>
      <rect class="band band--rust" x="0" y="1440" width="1050" height="25" fill="var(--rust)" opacity="0.7"/>
    </g>

    <!-- central disc -->
    <circle class="disc-ring" cx="527" cy="600" r="470" fill="var(--ring)"/>
    <circle class="disc" cx="527" cy="600" r="450" fill="url(#disc-tone)"/>

    <!-- heading -->
    <text class="script-line" x="512" y="338" font-size="96" text-anchor="middle" textLength="370" lengthAdjust="spacingAndGlyphs">Traditional</text>

    <ellipse class="wheat-sprig" cx="168" cy="475" rx="26" ry="80" transform="rotate(-20 168 475)" fill="var(--wheat)" role="img" aria-label="Hand-drawn wheat sprig"/>
    <ellipse class="wheat-sprig" cx="868" cy="475" rx="26" ry="80" transform="rotate(20 868 475)" fill="var(--wheat)" role="img" aria-label="Hand-drawn wheat sprig"/>

    <text class="product-name" x="258" y="585" font-size="250" textLength="550" lengthAdjust="spacingAndGlyphs">FLAT</text>
    <text class="product-name" x="162" y="828" font-size="250" textLength="712" lengthAdjust="spacingAndGlyphs">BREAD</text>

    <text class="tagline" x="520" y="908" font-size="46" text-anchor="middle" textLength="575" lengthAdjust="spacingAndGlyphs">HANDCRAFTED WITH</text>
    <text class="tagline" x="520" y="955" font-size="46" text-anchor="middle" textLength="470" lengthAdjust="spacingAndGlyphs">ANCIENT GRAINS</text>

    <!-- flatbread stack -->
    <path class="bread-stack" d="M150 1095 Q 260 1000 480 980 Q 760 968 900 1040 Q 945 1075 935 1130 Q 950 1170 935 1200 Q 950 1240 935 1270 Q 950 1320 925 1355 Q 880 1400 600 1405 Q 260 1410 140 1365 Q 112 1330 122 1290 Q 108 1250 125 1215 Q 110 1180 128 1150 Q 125 1115 150 1095 Z" fill="url(#bread-tone)" role="img" aria-label="Stack of golden flatbreads sprinkled with chopped parsley"/>

    <!-- net weight -->
    <rect class="net-weight-band" x="420" y="1408" width="200" height="34" rx="4" fill="var(--navy-deep)"/>
    <text class="net-weight" x="520" y="1433" font-size="22" text-anchor="middle">Net Wt. 10 oz (283 g)</text>
  </svg>
</main>
</body>
</html>
```